I need a website designed. I am a mortgage loan officer and would like to have a website for me and my team where i can post resources, videos and blog information for my clients. A website like thelorvikteam.com .

The theme is - The Pellam Team - Home Loan Group powered by Brightmoor Home Loans -

Target Market(s)

B2B (Real Estate Agents)and B2C (Home buyers and refinancing)

Industry/Entity Type

Mortgage Lender

Coding

Coded - Design and coding required

Number of Pages Required

5+ page

Font styles to use
Serif
Sans Serif

Colors

Designer to choose colors to be used in the design.

Requirements
Must have
• Disclaimers: Licensed by the Office of Commerce Stewardship under the Westland Credit Providers Act. Loans made or arranged pursuant to a Westland Credit Providers Act License. Equal Housing Lender Brightmoor Cannot Accept mortgage applications for properties located in New York via this site
• Mobile Friendly
Nice to have
• Main Links: Home, About Us(see team flyer), Mortgage 101, Contact Us (formly form)

```html
<!DOCTYPE html>
<html lang="en">
<head>
<meta charset="utf-8">
<title>The Pellam Team Home Loan Group</title>
<link href="https://fonts.googleapis.com/css2?family=Open+Sans:wght@400;600;700;800&display=swap" rel="stylesheet">
<style>
:root{
  --blue:#1a7fe0;
  --blue-deep:#0b5fc0;
  --navy:#0d4c9c;
  --heading:#1560b8;
  --yellow:#ffe600;
  --ink:#333;
  --muted:#666;
  --light:#f4f5f7;
  --footer:#5b5b5b;
  --white:#fff;
}
*{box-sizing:border-box;margin:0;padding:0}
html,body{width:1200px;height:2247px;overflow:hidden}
body{font-family:"Open Sans",Arial,sans-serif;color:var(--ink);background:var(--white);position:relative}
.brand{display:flex;align-items:center;gap:10px;color:var(--white);font-weight:700;font-size:18px;letter-spacing:.5px;text-transform:uppercase}
.brand-mark{width:16px;height:16px;background:var(--white)}

/* hero */
.hero{position:absolute;left:0;top:0;width:1200px;height:501px;background:linear-gradient(180deg,#2f95f0 0%,#1779dc 55%,#1169cc 100%);color:var(--white);text-align:center}
.hero-photo{position:absolute;inset:0;background:radial-gradient(ellipse at 30% 60%,rgba(255,255,255,.18),transparent 55%),radial-gradient(ellipse at 80% 40%,rgba(255,255,255,.12),transparent 50%)}
.site-nav{position:absolute;left:209px;right:209px;top:30px;display:flex;justify-content:space-between;align-items:center}
.nav-links{display:flex;gap:22px;align-items:center;font-size:11px;font-weight:700;text-transform:uppercase}
.nav-phone{color:var(--yellow);display:flex;align-items:center;gap:5px;font-size:12px}
.hero-title{position:absolute;top:226px;width:100%;font-size:36px;font-weight:700}
.hero-sub{position:absolute;top:281px;width:100%;font-size:15px;font-weight:600}
.btn{display:inline-block;background:var(--yellow);color:var(--navy);font-weight:700;font-size:13px;text-transform:uppercase;border-radius:20px;padding:11px 34px}
.hero .btn{position:absolute;left:503px;top:335px;width:164px;padding:11px 0}
.scroll-down{position:absolute;left:556px;top:419px;width:50px;height:50px;border-radius:50%;background:rgba(255,255,255,.25);display:flex;align-items:center;justify-content:center}

/* videos */
.videos{position:absolute;top:501px;left:0;width:1200px;height:321px;background:var(--white)}
.video{position:absolute;top:65px;width:247px;text-align:center}
.video-thumb{height:160px;background:linear-gradient(135deg,#6f6a63,#3c3833);display:flex;align-items:center;justify-content:center;box-shadow:0 8px 10px -6px rgba(0,0,0,.35)}
.video-thumb span{width:46px;height:46px;border:2px solid var(--white);border-radius:50%;display:flex;align-items:center;justify-content:center}
.video-title{margin-top:22px;font-size:13px;color:var(--heading)}

/* team */
.team{position:absolute;top:822px;left:0;width:1200px;height:695px;background:linear-gradient(180deg,#f2f2f2 0%,#e9e6e2 40%,#ddd4c8 100%)}
.section-title{font-size:26px;font-weight:700;color:var(--heading);text-align:center}
.team .section-title{position:absolute;top:66px;width:100%}
.member{position:absolute;top:155px;width:178px;height:281px;background:var(--white);text-align:center;box-shadow:0 2px 8px rgba(0,0,0,.12)}
.member-photo{width:148px;height:135px;margin:14px auto 0;background:linear-gradient(180deg,#c9c3bd,#8b8580)}
.member-name{margin-top:10px;font-size:14px;font-weight:700;color:var(--heading)}
.member-role{font-size:9px;line-height:14px;color:var(--ink);margin-top:3px}
.member-btn{display:inline-block;margin-top:12px;border:1px solid #9fc3ea;border-radius:12px;padding:3px 22px;font-size:9px;color:var(--heading)}
.guide{position:absolute;top:499px;width:100%;text-align:center}
.guide h2{font-size:24px;font-weight:700;color:var(--heading)}
.guide p{font-size:12px;line-height:18px;margin:14px auto 0;width:430px;color:var(--muted)}
.guide .btn{margin-top:24px;padding:10px 28px}

/* testimonials */
.testimonials{position:absolute;top:1517px;left:0;width:1200px;height:366px;background:var(--light)}
.testimonials .section-title{position:absolute;top:46px;width:100%;font-size:21px}
.quote-wing{position:absolute;top:173px;width:60px;height:108px;background:#b8c6de}
.quote-card{position:absolute;left:355px;top:110px;width:515px;height:184px;background:linear-gradient(135deg,#2d8ee8,#1569c8);color:var(--white);box-shadow:0 6px 14px rgba(0,0,0,.25)}
.quote-avatar{position:absolute;left:34px;top:52px;width:76px;height:76px;border-radius:50%;background:linear-gradient(180deg,#d5e5f5,#9fb9d4);border:3px solid var(--white)}
.quote-text{position:absolute;left:124px;top:50px;width:360px;text-align:center;font-size:11px;line-height:17px}
.quote-name{margin-top:8px;font-weight:700;font-size:10px}
.quote-role{margin-top:6px;font-size:9px;border-top:1px solid rgba(255,255,255,.6);padding-top:6px;display:inline-block}
.quote-mark{position:absolute;left:108px;top:10px}
.dots{position:absolute;top:317px;left:0;width:100%;display:flex;justify-content:center;gap:4px}
.dots span{width:9px;height:9px;border-radius:50%;border:1px solid var(--blue)}
.dots span:first-child{background:var(--blue)}

/* partners */
.partners{position:absolute;top:1883px;left:0;width:1200px;height:146px;background:var(--white);display:flex;justify-content:center;align-items:center;gap:60px}
.partner{background:#d8d8d8;height:58px}

/* footer */
.site-footer{position:absolute;top:2029px;left:0;width:1200px;height:218px;background:var(--footer);border-top:4px solid var(--blue);color:var(--white);text-align:center}
.site-footer .brand{justify-content:center;margin-top:40px;font-size:17px}
.footer-links{margin-top:30px;display:flex;justify-content:center;gap:22px;font-size:11px;font-weight:600}
.footer-contact{margin-top:12px;font-size:11px}
.footer-contact b{font-weight:700}
.disclaimer{width:790px;margin:14px auto 0;font-size:9px;line-height:13px;border-top:1px solid rgba(255,255,255,.25);padding-top:8px}
</style>
</head>
<body>

<header class="hero">
  <div class="hero-photo" role="img" aria-label="Bright living room interior tinted blue"></div>
  <nav class="site-nav">
    <div class="brand"><span class="brand-mark"></span>The Pellam Team</div>
    <div class="nav-links">
      <span>Home</span><span>About Us</span><span>Mortgage 101</span><span>Contact Us</span>
      <span class="nav-phone">
        <svg width="11" height="11" viewBox="0 0 24 24"><path fill="#ffe600" d="M6.6 10.8a15 15 0 006.6 6.6l2.2-2.2a1 1 0 011-.25 11.4 11.4 0 003.6.6 1 1 0 011 1V20a1 1 0 01-1 1A17 17 0 013 4a1 1 0 011-1h3.5a1 1 0 011 1c0 1.25.2 2.45.6 3.6a1 1 0 01-.25 1z"/></svg>
        1-555-014-7290
      </span>
    </div>
  </nav>
  <h1 class="hero-title">The Pellam Team Home Loan Group</h1>
  <p class="hero-sub">We're Not Going To Do What's Easy For Us; We're Going To Do What's Best For You.</p>
  <span class="btn">Call Us Today</span>
  <span class="scroll-down"><svg width="20" height="12" viewBox="0 0 20 12"><path d="M2 2l8 8 8-8" stroke="#fff" stroke-width="2" fill="none"/></svg></span>
</header>

<section class="videos">
  <div class="video" style="left:211px">
    <div class="video-thumb" role="img" aria-label="Video still of a couple unpacking moving boxes"><span><svg width="16" height="18" viewBox="0 0 16 18"><path d="M2 1l13 8-13 8z" fill="#fff"/></svg></span></div>
    <p class="video-title">First Time Homebuyer 101</p>
  </div>
  <div class="video" style="left:476px">
    <div class="video-thumb" role="img" aria-label="Video still of a home interior hallway"><span><svg width="16" height="18" viewBox="0 0 16 18"><path d="M2 1l13 8-13 8z" fill="#fff"/></svg></span></div>
    <p class="video-title">FHA Financing 101</p>
  </div>
  <div class="video" style="left:742px">
    <div class="video-thumb" role="img" aria-label="Video still of a living room with stairs"><span><svg width="16" height="18" viewBox="0 0 16 18"><path d="M2 1l13 8-13 8z" fill="#fff"/></svg></span></div>
    <p class="video-title">Top 10 Mortgage Questions</p>
  </div>
</section>

<section class="team" role="img" aria-label="Soft kitchen interior background">
  <h2 class="section-title">The Pellam Team</h2>
  <article class="member" style="left:211px">
    <div class="member-photo" role="img" aria-label="Portrait of Marco Pellam"></div>
    <h3 class="member-name">Marco Pellam</h3>
    <p class="member-role">Producing Branch Manager<br>Brightmoor Home Loans, Inc. - NMLS 40012</p>
    <span class="member-btn">+Detail</span>
  </article>
  <article class="member" style="left:411px">
    <div class="member-photo" role="img" aria-label="Portrait of Dario Venn"></div>
    <h3 class="member-name">Dario Venn</h3>
    <p class="member-role">Producing Branch Manager<br>Loan Partner NMLS ID 5520187</p>
    <span class="member-btn">+Detail</span>
  </article>
  <article class="member" style="left:611px">
    <div class="member-photo" role="img" aria-label="Portrait of Tomas Ruelle"></div>
    <h3 class="member-name">Tomas Ruelle</h3>
    <p class="member-role">Producing Branch Manager<br>Loan Processor NMLS ID 6634021</p>
    <span class="member-btn">+Detail</span>
  </article>
  <article class="member" style="left:811px">
    <div class="member-photo" role="img" aria-label="Portrait of Lena Harrow"></div>
    <h3 class="member-name">Lena Harrow</h3>
    <p class="member-role">Producing Branch Manager<br>Team Leader NMLS ID 6634021</p>
    <span class="member-btn">+Detail</span>
  </article>
  <div class="guide">
    <h2>Top 5 Common Mortgage Mistakes to Avoid</h2>
    <p>We don't need an e-mail address; we want you to feel safe, secure, and comfortable when choosing a home loan.</p>
    <span class="btn">Download Now</span>
  </div>
</section>

<section class="testimonials">
  <h2 class="section-title">What our Client say About Us</h2>
  <div class="quote-wing" style="left:326px"></div>
  <div class="quote-wing" style="left:840px"></div>
  <div class="quote-card">
    <svg class="quote-mark" width="46" height="36" viewBox="0 0 46 36"><path fill="rgba(255,255,255,.25)" d="M0 36V20C0 8 6 1 18 0v7c-6 1-9 5-9 11h9v18zm26 0V20C26 8 32 1 44 0v7c-6 1-9 5-9 11h9v18z"/></svg>
    <div class="quote-avatar" role="img" aria-label="Client portrait"></div>
    <div class="quote-text">
      They made the whole process so easy for me and looked for so many different ways to make it even easier. I appreciate all the help that they provided me. They truly helped make this experience great!
      <p class="quote-name">Jordan Ames</p>
      <p class="quote-role">Founder</p>
    </div>
  </div>
  <div class="dots"><span></span><span></span><span></span></div>
</section>

<section class="partners" aria-label="Partners and awards">
  <div class="partner" style="width:100px"></div>
  <div class="partner" style="width:130px"></div>
  <div class="partner" style="width:110px"></div>
  <div class="partner" style="width:140px"></div>
</section>

<footer class="site-footer">
  <div class="brand"><span class="brand-mark"></span>The Pellam Team</div>
  <nav class="footer-links"><span>Home</span><span>About Us</span><span>Mortgage 101</span><span>Contact Us</span></nav>
  <p class="footer-contact"><b>1-555-014-7290</b> &nbsp;|&nbsp; 4810 Alder Crest Rd, Suite 120, Fairhaven FL 30410</p>
  <p class="disclaimer">Disclaimers: Licensed by the Office of Commerce Stewardship under the Westland Credit Providers Act. Loans made or arranged pursuant to a Westland Credit Providers Act License. Equal Housing Lender Brightmoor Cannot Accept mortgage applications for properties located in New York via this site</p>
</footer>

</body>
</html>
```